Open House evite for our 7th Anniversary needs Invitation Design

Need an invitation design for an upcoming event. Our event is an Open House to celebrate our 7th anniversary with clients & business colleagues. We need a professional but fun invitation. We are a women owned law firm. We will use this design for a Save the Date, an evite, a hard invitation, an eReminder and a wine label.
Focus of design should be on the "7"!!! (this is new)
Every year the focus will be on the year.
We have 3 women partners who run the firm. If there is a way to incorporate that into the drawing-great! Attached is a sketch that focuses on the 7 and has three stick figure women. It has our logo "&" in the background and says "Seven Lucky Years & Still Going...." OPEN HOUSE....This is a thought, please play around with it. It does not have to have the women, but is one thought. We have a submittal on an elegant 7 that we liked, but did not hear back from the designer, so that is an option also. An elegant 7 in black, gray background, with blue or green as accent colors is something else we would like to see.

Please view our website: www.bhqcounsel.example for our colors. You do not need to use these, but it gives you an idea of the feel of our marketing.
Incorporate:
our logo, per attached

OPEN HOUSE:
June 4, 2015
3:00-7:00pm
Brenner, Hollis & Quade, LLC
4812 Tamarack, Suite 300
Rolling Meadows, IL 60008
RSVP to rsvp@bhqcounsel.example

We will only be sending out about 20 actual hard copy invites. We will be sending the evites through Steady Mailer and this is the heart of the project. We will send a Save the Date, then 2-3 weeks later an evite, then 2-4 weeks later a Reminder, and then the week before one more reminder.
The wine labels are used all year long and are the past years are all displayed in frames in our office. They are an important aspect of our marketing efforts.

Target Market(s)

Adults - clients & business colleagues

Industry/Entity Type

Business

Colors
000000
acd036
81c7e5

Requirements
Must have
• Focus the design on the "7". There is a sketched attached. This is not exactly what we want, but a thought. See attached.
• Incorporate our logo, per attached
• OPEN HOUSE:
• June 4, 2015
• 3:00-7:00pm
• Brenner, Hollis & Quade, LLC
• 4812 Tamarack, Suite 300
• Rolling Meadows, IL 60008
• RSVP to rsvp@bhqcounsel.example
Nice to have
• If you can incorporate 3 women lawyer figures into the design - great! Stick figures are ok.

```html
<!DOCTYPE html>
<html lang="en">
<head>
<meta charset="utf-8">
<title>Save the Date – 7th Anniversary Open House</title>
<link rel="stylesheet" href="https://fonts.googleapis.com/css2?family=Lato:ital,wght@0,100;0,300;0,400;0,700;1,400&display=swap">
<style>
  :root {
    --charcoal: #3b3b3c;
    --charcoal-deep: #333334;
    --accent-green: #8fb22a;
    --date-green: #a9cb3a;
    --title-blue: #6a8fcb;
    --muted-gray: #8c8c8c;
    --label-gray: #a3a3a3;
    --soft-white: #ececec;
    --note-gray: #cfcfcf;
    --paper: #ffffff;
    --brand-blue: #34557f;
    --footer-gray: #4f4f4f;
  }
  * { margin: 0; padding: 0; box-sizing: border-box; }
  html, body { width: 1067px; height: 1200px; overflow: hidden; background: var(--paper); }
  body { font-family: "Lato", Helvetica, Arial, sans-serif; }

  .card {
    position: relative;
    width: 1067px;
    height: 1200px;
    overflow: hidden;
    background: var(--paper);
  }

  .card__stage {
    position: absolute;
    left: 0; top: 0;
    width: 1067px; height: 1090px;
    background:
      repeating-linear-gradient(90deg, rgba(255,255,255,0.018) 0 2px, rgba(0,0,0,0.03) 2px 5px),
      repeating-linear-gradient(0deg, rgba(0,0,0,0.025) 0 3px, rgba(255,255,255,0.012) 3px 7px),
      var(--charcoal);
  }

  .card__flourish {
    position: absolute;
    left: 0; top: 0;
    width: 1067px; height: 114px;
    background: radial-gradient(ellipse 60% 100% at 50% 0%, var(--accent-green) 0%, rgba(143,178,42,0.75) 55%, rgba(143,178,42,0) 100%);
  }

  .headline {
    position: absolute;
    left: 0; width: 100%;
    text-align: center;
    font-weight: 100;
    font-size: 262px;
    line-height: 1;
    letter-spacing: 6px;
    color: var(--title-blue);
  }
  .headline--save { top: 146px; }
  .headline--date { top: 454px; }

  .divider {
    position: absolute;
    left: 0; top: 400px;
    width: 1067px; height: 36px;
  }
  .divider__badge {
    position: absolute;
    left: 505px; top: 366px;
    width: 102px; height: 102px;
    border-radius: 50%;
    background: var(--muted-gray);
    color: var(--soft-white);
    font-weight: 300;
    font-size: 48px;
    line-height: 96px;
    text-align: center;
  }

  .event-line {
    position: absolute;
    left: 0; width: 100%;
    text-align: center;
    line-height: 1;
  }
  .event-line--numeric { top: 708px; font-size: 41px; color: var(--date-green); font-weight: 400; }
  .event-line--spelled { top: 759px; font-size: 29px; color: var(--muted-gray); font-weight: 400; }
  .event-line--label   { top: 854px; font-size: 30px; color: var(--label-gray); font-weight: 700; letter-spacing: 0.5px; }
  .event-line--title   { top: 898px; font-size: 38px; color: var(--soft-white); font-weight: 400; }
  .event-line--note    { top: 990px; font-size: 27px; color: var(--note-gray); font-style: italic; }
  .event-line--note svg { vertical-align: -3px; margin-right: 14px; }

  .card__band {
    position: absolute;
    left: 0; top: 1040px;
    width: 1067px; height: 50px;
  }

  .brand {
    position: absolute;
    left: 60px; top: 1112px;
    display: flex;
    align-items: center;
    gap: 12px;
  }
  .brand__mark {
    width: 26px; height: 26px;
    background: var(--brand-blue);
  }
  .brand__name {
    font-size: 24px;
    font-weight: 700;
    color: var(--brand-blue);
    line-height: 1;
  }

  .partners {
    position: absolute;
    right: 58px; top: 1124px;
    font-size: 20px;
    letter-spacing: 1px;
    color: var(--footer-gray);
    line-height: 1;
  }
  .partners__dot { color: var(--accent-green); }
</style>
</head>
<body>
  <main class="card">
    <section class="card__stage">
      <div class="card__flourish" role="img" aria-label="Green ornamental scrollwork flourish along the top edge"></div>

      <h1 class="headline headline--save">SAVE</h1>

      <svg class="divider" viewBox="0 0 1067 36" aria-hidden="true">
        <defs>
          <linearGradient id="rule-left" x1="0" x2="1">
            <stop offset="0" stop-color="#e6e6e6"/>
            <stop offset="0.85" stop-color="#e6e6e6"/>
            <stop offset="1" stop-color="#e6e6e6" stop-opacity="0"/>
          </linearGradient>
          <linearGradient id="rule-right" x1="0" x2="1">
            <stop offset="0" stop-color="#e6e6e6" stop-opacity="0"/>
            <stop offset="0.15" stop-color="#e6e6e6"/>
            <stop offset="1" stop-color="#e6e6e6"/>
          </linearGradient>
        </defs>
        <rect x="56" y="22" width="420" height="1.5" fill="url(#rule-left)"/>
        <rect x="636" y="22" width="374" height="1.5" fill="url(#rule-right)"/>
      </svg>
      <div class="divider__badge">the</div>

      <h2 class="headline headline--date">DATE</h2>

      <p class="event-line event-line--numeric">06.14.2015</p>
      <p class="event-line event-line--spelled">June fourteen two thousand fifteen</p>
      <p class="event-line event-line--label">[ OPEN HOUSE ]</p>
      <p class="event-line event-line--title">7th Anniversary Celebration</p>
      <p class="event-line event-line--note">
        <svg width="30" height="22" viewBox="0 0 30 22" aria-hidden="true">
          <rect x="1" y="1" width="28" height="20" fill="none" stroke="#cfcfcf" stroke-width="1.6"/>
          <path d="M1 1 L15 12 L29 1 M1 21 L11 10 M29 21 L19 10" fill="none" stroke="#cfcfcf" stroke-width="1.6"/>
        </svg>Formal invitation to follow.
      </p>
    </section>

    <svg class="card__band" viewBox="0 0 1067 50" aria-hidden="true">
      <polygon points="0,7 1067,7 1067,20 0,44" fill="var(--accent-green)"/>
      <polygon points="0,44 1067,20 1067,50 0,50" fill="var(--paper)"/>
    </svg>

    <footer>
      <div class="brand">
        <span class="brand__mark"></span>
        <span class="brand__name">Brenner Hollis Quade</span>
      </div>
      <p class="partners">BRENNER <span class="partners__dot">•</span> HOLLIS <span class="partners__dot">•</span> QUADE</p>
    </footer>
  </main>
</body>
</html>
```